Modern Medical Optometry Website

We need mordern, Patient friendly website. Easy to navigate and enhance our advance medical technology and excellent patient care.
1. HOME PAGE
2. OUR TEAM PAGE
3. EYECARE PAGE - VISION SERVICES, EYE EXAMS, KERATOCONUS CENTER, GLAUCOMA , DIABITES, TORVANEX EXAM, DIGITAL RETINAL, OCT.
4. MYOPIA CONTROL CLINIC
5. DRY EYE CLINIC
6. EYEWEAR
7. PATIENT CENTER - BLOG
7. CONTACT US
This is our current website www.brindlecove.com
and We want to add more content and a cleaner design like these website
http://tamsworthoptometry.com/
https://www.klmhaven.com/

```html
<!DOCTYPE html>
<html lang="en">
<head>
<meta charset="utf-8">
<title>Brindlecove Optometry</title>
<link rel="stylesheet" href="https://fonts.googleapis.com/css2?family=Open+Sans:wght@300;400;600;700&display=swap">
<style>
:root{
  --gold:#e8c048;
  --gold-dark:#c99a1c;
  --gold-text:#e0b02c;
  --ink:#444;
  --muted:#999;
  --soft:#f5f5f5;
  --line:#e4e4e4;
  --footer:#3b3b3b;
  --blue:#1f86d8;
}
*{box-sizing:border-box;margin:0;padding:0}
html,body{width:1200px;height:1200px;overflow:hidden;background:#fff}
body{font-family:"Open Sans",sans-serif;color:var(--ink);position:relative}
.abs{position:absolute}
.tiny{font-size:4.6px;line-height:8.2px;color:var(--muted)}
.topbar{top:44px;left:427px;font-size:4.6px;color:var(--muted)}
.social-top{top:43px;left:786px;display:flex;gap:7px}
.dot{width:6px;height:6px;border-radius:50%;background:#aaa}
.rule{height:1px;background:var(--line)}
.logo{display:flex;flex-direction:column;align-items:center;gap:3px}
.logo-mark{width:18px;height:18px;background:var(--gold)}
.logo-name{font-size:5px;color:var(--gold-text);letter-spacing:.4px}
.nav{top:72px;left:580px;display:flex;gap:0;font-size:6.6px;color:#555}
.nav span{position:absolute;white-space:nowrap}
.nav .active{color:var(--gold-text)}
.hero-band{left:346px;top:96px;width:592px;height:177px;background:linear-gradient(90deg,#e6e6e6,#f6f6f6 15%,#f6f6f6 85%,#e6e6e6)}
.hero-photo{left:425px;top:96px;width:433px;height:148px;background:linear-gradient(100deg,#f1f1f1 0%,#e9e4de 30%,#d9a77a 48%,#e8d4bd 60%,#eeeeee 80%,#dcd8d2 100%)}
.side-strip{left:930px;top:96px;width:6px;height:321px;background:#efefef}
.card{top:244px;width:107px;height:94px;background:var(--gold);color:#fff;padding:10px 12px}
.card h3{font-weight:400;font-size:10px;line-height:12px;margin-bottom:4px}
.card p{font-size:6.6px;line-height:9.6px}
.card .btn{position:absolute;left:12px;top:71px;width:73px;height:17px;border:1px solid #fff;font-size:7px;line-height:15px;padding-left:5px}
.card .fold{position:absolute;right:0;bottom:0}
.sched-row{display:flex;justify-content:space-between;font-size:5px;border-bottom:1px solid rgba(255,255,255,.7);padding:3px 0 6px}
.center{left:346px;width:592px;text-align:center}
.h-light{font-weight:300;font-size:14px;color:#444}
.gray{background:var(--soft)}
.blog-thumb{width:31px;height:31px;background:linear-gradient(135deg,#cfe3f0,#f0f0f0)}
.blog-title{font-size:8.8px;color:#333}
.acc{left:642px;width:205px;height:15px;border:1px solid var(--line);background:#fff;font-size:6px;color:var(--gold-text);line-height:13px;padding-left:5px}
.acc .tick{display:inline-block;width:12px;color:var(--gold-text)}
.acc .plus{position:absolute;right:6px;top:0;color:var(--gold-text);font-size:8px}
.acc.open{background:var(--gold);color:#fff;border-color:var(--gold)}
.acc.open .tick,.acc.open .plus{color:#fff}
.team-card{top:728px;width:88px;height:104px;border:1px solid var(--line);background:#fff}
.team-photo{width:86px;height:87px;background:linear-gradient(180deg,#e4eef6,#f4f7fa 60%,#dfe6ec)}
.team-name{font-size:5.6px;color:var(--gold-text);text-align:center;margin-top:6px}
.arrow{top:775px;width:9px;height:11px;border:1px solid #ccc;background:#fff;font-size:6px;color:#999;text-align:center;line-height:9px}
.avatar{width:30px;height:30px;border-radius:50%;background:linear-gradient(160deg,#c8c8c8,#8b8b8b)}
.t-name{font-size:5.4px;color:#888;text-align:center;width:60px}
.t-site{font-size:4.6px;color:#aaa;font-style:italic;text-align:center;width:60px}
.footer{left:346px;top:1038px;width:586px;height:162px;background:var(--footer)}
.f-head{font-size:5.2px;font-weight:600;color:#fff;letter-spacing:.2px}
.f-text{font-size:4.6px;line-height:8.4px;color:#ccc}
.f-thumb{width:26px;height:26px;background:linear-gradient(135deg,#cfe0ec,#f2f2f2)}
.f-icon{width:5px;height:5px;border-radius:50%;background:#ddd;display:inline-block;margin-right:5px;vertical-align:middle}
</style>
</head>
<body>

<!-- Header -->
<div class="abs topbar">&#9742; 1800-555-014 &nbsp;&nbsp; &#9993; hello@brindlecove.com</div>
<div class="abs social-top"><span class="dot"></span><span class="dot"></span><span class="dot"></span><span class="dot"></span><span class="dot"></span></div>
<div class="abs rule" style="left:427px;top:54px;width:501px"></div>
<div class="abs logo" style="left:432px;top:58px;width:64px">
  <div class="logo-mark"></div>
  <div class="logo-name">BRINDLECOVE</div>
</div>
<div class="abs rule" style="left:577px;top:54px;width:28px;height:2px;background:var(--gold)"></div>
<nav class="abs nav">
  <span class="active" style="left:0">Home</span>
  <span style="left:34px">About Us</span>
  <span style="left:79px">Services</span>
  <span style="left:121px">Eyecare Department</span>
  <span style="left:196px">Blog</span>
  <span style="left:223px">Contact</span>
  <span style="left:263px">&#9906;</span>
</nav>

<!-- Hero -->
<div class="abs hero-band"></div>
<div class="abs hero-photo" role="img" aria-label="Photo of a smiling mother and daughter beside eye examination equipment in a bright clinic"></div>
<div class="abs side-strip"></div>

<div class="abs card" style="left:426px">
  <h3>Emergent Case</h3>
  <p>This is the clinic's vesollicitudin, bibendum auctor, ntorquent per coaliquam massa nisl</p>
  <div class="btn">Read More</div>
  <svg class="fold" width="10" height="10"><polygon points="10,0 10,10 0,10" fill="#fff"/><polygon points="0,10 10,0 0,0" fill="var(--gold-dark)"/></svg>
</div>
<div class="abs card" style="left:534px">
  <h3>Consultancy</h3>
  <p>This is the clinic's vesollicitudin, bibendum auctor, ntorquent per coaliquam massa nisl</p>
  <div class="btn">Read More</div>
  <svg class="fold" width="10" height="10"><polygon points="10,0 10,10 0,10" fill="#fff"/><polygon points="0,10 10,0 0,0" fill="var(--gold-dark)"/></svg>
</div>
<div class="abs card" style="left:642px">
  <h3>Appointment</h3>
  <p>This is the clinic's vesollicitudin, bibendum auctor, ntorquent per coaliquam massa nisl</p>
  <div class="btn">Read More</div>
  <svg class="fold" width="10" height="10"><polygon points="10,0 10,10 0,10" fill="#fff"/><polygon points="0,10 10,0 0,0" fill="var(--gold-dark)"/></svg>
</div>
<div class="abs card" style="left:750px">
  <h3>Time Schedule</h3>
  <div class="sched-row" style="margin-top:6px"><span>Mon-Fri</span><span>8:00 - 18:00</span></div>
  <div class="sched-row" style="margin-top:6px"><span>Sat</span><span>8:00 - 18:00</span></div>
  <div class="sched-row" style="margin-top:4px;border:0"><span>Sun</span><span>8:00 - 18:00</span></div>
  <svg class="fold" width="10" height="10"><polygon points="10,0 10,10 0,10" fill="#fff"/><polygon points="0,10 10,0 0,0" fill="var(--gold-dark)"/></svg>
</div>

<!-- About -->
<h2 class="abs center h-light" style="top:366px">About Us &amp; What We Do</h2>
<p class="abs tiny" style="left:426px;top:390px;width:424px;text-align:center">Lorem ipsum is simply dummy text of the printing and typesetting industry. Lorem ipsum has been the industry's standard dummy text ever since the 1500s, when an unknown printer took a galley of type and scrambled it to make a type specimen book.</p>

<!-- Blog + Departments -->
<section class="abs gray" style="left:345px;top:442px;width:589px;height:236px"></section>
<h2 class="abs" style="left:427px;top:449px;font-weight:300;font-size:11.5px;color:#555">LATEST BLOG</h2>

<div class="abs blog-thumb" style="left:427px;top:476px" role="img" aria-label="Blog thumbnail: doctor measuring a patient's blood pressure"></div>
<div class="abs blog-title" style="left:465px;top:474px">Monitor Your Blood Pressure</div>
<p class="abs tiny" style="left:465px;top:501px;width:162px">Donec rutrum congue leo eget malesuada. Donec sollicitudin molestie malesuada. Mauris blandit aliquet elit, eget tincidunt nibh pulvinar a. Curabitur aliquet quam id dui ...</p>
<div class="abs tiny" style="left:465px;top:532px;font-size:4px">Posted in: Blood Pressure</div>
<div class="abs rule" style="left:465px;top:544px;width:163px"></div>

<div class="abs blog-thumb" style="left:427px;top:557px" role="img" aria-label="Blog thumbnail: smiling children at an eye clinic"></div>
<div class="abs blog-title" style="left:465px;top:556px">Each Child Is Special, so Keep Care</div>
<p class="abs tiny" style="left:465px;top:583px;width:162px">Intrinsicly initiate cooperative imperatives vis-a-vis backend resources. Dramatically syndicate backward-compatible web-readiness with mission-critical scenarios. Effici...</p>
<div class="abs tiny" style="left:465px;top:614px;font-size:4px">Posted in: Pediatric Medication</div>
<div class="abs rule" style="left:465px;top:626px;width:163px"></div>

<h2 class="abs h-light" style="left:642px;top:448px">Departments</h2>
<div class="abs acc" style="top:476px"><span class="tick">&#10003;</span>VISION SERVICES<span class="plus">+</span></div>
<div class="abs acc" style="top:491px"><span class="tick">&#10003;</span>EYE EXAMS<span class="plus">+</span></div>
<div class="abs acc open" style="top:507px"><span class="tick">&#10003;</span>KERATOCONUS CENTER<span class="plus">&minus;</span></div>
<div class="abs" style="left:646px;top:530px;width:62px;height:58px;background:linear-gradient(135deg,#e9eef2,#c9b6a3 55%,#eef1f4)" role="img" aria-label="Photo of a patient during an eye examination with a trial frame"></div>
<div class="abs" style="left:716px;top:530px;font-size:6px;font-weight:700;color:#333">Donec scelerisque, leo non eleifend</div>
<p class="abs tiny" style="left:716px;top:541px;width:130px">Lorem ipsum dolor sit amet, consecte tur adipiscing elit ut eu nisl quis augue suscipit dignissim. Duis vulputate nisl sit amet feugiat tincidunt.</p>
<div class="abs" style="left:716px;top:575px;width:39px;height:13px;border:1px solid var(--gold-text);font-size:5px;color:var(--gold-text);line-height:11px;text-align:center">READ MORE</div>
<div class="abs acc" style="top:610px"><span class="tick">&#10003;</span>GLAUCOMA<span class="plus">+</span></div>
<div class="abs acc" style="top:625px"><span class="tick">&#10003;</span>DIABITES<span class="plus">+</span></div>
<div class="abs acc" style="top:640px"><span class="tick">&#10003;</span>TORVANEX EXAM<span class="plus">+</span></div>

<!-- Team -->
<h2 class="abs center" style="top:687px;font-weight:400;font-size:11px;color:var(--gold-text)">MEET OUR TEAM</h2>
<p class="abs tiny center" style="top:705px">Lorem ipsum is simply dummy text of the printing and typesetting industry lorem ipsum has been the industry's standard dummy text ever since the 1500s.</p>
<div class="abs arrow" style="left:432px">&lsaquo;</div>
<div class="abs arrow" style="left:828px">&rsaquo;</div>
<div class="abs team-card" style="left:442px"><div class="team-photo" role="img" aria-label="Portrait of a female doctor with stethoscope"></div><div class="team-name">MARA LINDQVIST</div></div>
<div class="abs team-card" style="left:541px"><div class="team-photo" role="img" aria-label="Portrait of a male doctor with stethoscope"></div><div class="team-name">OWEN HALBROOK</div></div>
<div class="abs team-card" style="left:640px"><div class="team-photo" role="img" aria-label="Portrait of a female doctor with stethoscope"></div><div class="team-name">MARA LINDQVIST</div></div>
<div class="abs team-card" style="left:739px"><div class="team-photo" role="img" aria-label="Portrait of a male doctor with stethoscope"></div><div class="team-name">OWEN HALBROOK</div></div>

<!-- Testimonials -->
<section class="abs gray" style="left:345px;top:863px;width:587px;height:169px"></section>
<h2 class="abs center h-light" style="top:888px">Testimonials &amp; Clients</h2>
<p class="abs tiny center" style="top:913px">Lorem ipsum is simply dummy text of the printing and typesetting industry lorem ipsum has been the industry's standard dummy text ever since the 1500s.</p>

<div class="abs avatar" style="left:436px;top:938px" role="img" aria-label="Client portrait"></div>
<div class="abs t-name" style="left:421px;top:972px">Jon Ellery</div>
<div class="abs t-site" style="left:421px;top:983px">Harborview Press</div>
<div class="abs t-site" style="left:421px;top:992px;font-style:normal;font-weight:700;color:#777">&rdquo;</div>
<p class="abs tiny" style="left:481px;top:937px;width:146px">Etiam tristique sagittis pulvinar. Cras at lectus rhoncus, scelerisque dui ut, bibendum ante. Ut vulputate blandit neque eget lobortis. Nam eleifend sollicitudin nulla quis luctus nam et. Interdum et malesuada fames ac ante ipsum primis in faucibus. Phas ellus ornare leo risus, at posuere dolor viverra quis. Suspendisse mattis bibendum ultrices. In hac habitasse quisque ut faucibus erat curabitur luctus.</p>

<div class="abs avatar" style="left:651px;top:938px" role="img" aria-label="Client portrait"></div>
<div class="abs t-name" style="left:636px;top:972px">Carl Pemberton</div>
<div class="abs t-site" style="left:636px;top:983px">Harborview Press</div>
<div class="abs t-site" style="left:636px;top:992px;font-style:normal;font-weight:700;color:#777">&rdquo;</div>
<p class="abs tiny" style="left:696px;top:937px;width:146px">Etiam tristique sagittis pulvinar. Cras at lectus rhoncus, scelerisque dui ut, bibendum ante. Ut vulputate blandit neque eget lobortis. Nam eleifend sollicitudin nulla quis luctus nam et. Interdum et malesuada fames ac ante ipsum primis in faucibus. Phas ellus ornare leo risus, at posuere dolor viverra quis. Suspendisse mattis bibendum ultrices. In hac habitasse quisque ut faucibus erat curabitur luctus.</p>

<!-- Footer -->
<footer class="abs footer"></footer>
<div class="abs logo" style="left:430px;top:1054px;width:56px">
  <div class="logo-mark" style="width:20px;height:20px"></div>
  <div class="logo-name">BRINDLECOVE</div>
</div>
<p class="abs f-text" style="left:427px;top:1090px;width:80px">Lorem ipsum dolor sit amet, teft consecte tur adipiscing.</p>
<div class="abs f-text" style="left:427px;top:1118px;width:90px">
  <div><span class="f-icon"></span>Larkfield Clinic</div>
  <div style="padding-left:10px">48 Orchard Lane</div>
  <div style="padding-left:10px">Fairhaven, NY 10422</div>
  <div style="margin-top:3px"><span class="f-icon"></span>1800-555-014</div>
  <div style="margin-top:3px"><span class="f-icon"></span>+1 945 555 762</div>
  <div style="margin-top:3px"><span class="f-icon"></span>hello@brindlecove.com</div>
</div>

<div class="abs f-head" style="left:532px;top:1068px">RECENT POSTS</div>
<div class="abs f-thumb" style="left:532px;top:1091px" role="img" aria-label="Post thumbnail"></div>
<p class="abs f-text" style="left:563px;top:1091px;width:55px;color:#fff">Monitor Your Blood Pressure<br>Dec 22, 2014</p>
<div class="abs f-thumb" style="left:532px;top:1122px" role="img" aria-label="Post thumbnail"></div>
<p class="abs f-text" style="left:563px;top:1122px;width:60px;color:#fff">Each Child Is Special, so Keep Care<br>Dec 20, 2014</p>
<div class="abs f-thumb" style="left:532px;top:1153px" role="img" aria-label="Post thumbnail"></div>
<p class="abs f-text" style="left:563px;top:1153px;width:55px;color:#fff">The New Cholesterol Guidelines<br>Dec 17, 2014</p>

<div class="abs f-head" style="left:637px;top:1068px">RECENT TWEETS</div>
<div class="abs f-text" style="left:636px;top:1092px">&rsaquo;</div>
<p class="abs f-text" style="left:647px;top:1091px;width:50px">RT<br><b style="color:#fff">@quiet_rowan</b><br>: Kicked off<br><b style="color:#fff">#openmonth</b><br>with a PR to<br><b style="color:#fff">#sitebuild</b><br>!<br><b style="color:#fff">@brightmeadow</b><br><span style="color:var(--gold)">&#9679;</span><br>2018-10-05</p>

<div class="abs f-head" style="left:742px;top:1068px">NEWSLETTER</div>
<p class="abs f-text" style="left:742px;top:1091px;width:100px">Lorem ipsum dolor sit amet, teft consecte tur adipiscing elit ut eunt.</p>
<div class="abs" style="left:742px;top:1112px;width:70px;height:12px;background:#fff;font-size:4.4px;color:#999;line-height:12px;padding-left:3px">Your email address</div>
<div class="abs" style="left:812px;top:1112px;width:30px;height:12px;background:var(--blue);font-size:4.4px;color:#fff;line-height:12px;text-align:center">subscribe</div>
<div class="abs f-head" style="left:742px;top:1145px">SOCIAL MEDIA</div>
<div class="abs" style="left:742px;top:1155px;display:flex;gap:8px">
  <span class="dot" style="background:#fff;width:7px;height:7px"></span>
  <span class="dot" style="background:#fff;width:7px;height:7px"></span>
  <span class="dot" style="background:#fff;width:7px;height:7px"></span>
  <span class="dot" style="background:#fff;width:7px;height:7px"></span>
  <span class="dot" style="background:#fff;width:7px;height:7px"></span>
</div>

</body>
</html>
```